Vertical Banner

I need an eye-catching banner created for street fairs, indoor and outdoor events to draw attention to our language school. It will be to print on this banner (specs included):
https://www.printvalemart.com/tag/317/Retractable-Banners/product/5146-71/Basic-Rollup-Banner-Stand-29-14

I want the banner to be:
- SIMPLE
- Eye catching (not busy with too many pictures or information)
- It should say at top prominently: "Come learn a language!" and have our name.
- Below these languages should be large and eye-catching: Spanish, Chinese, French, Russian, German, Italian, Farsi, Turkish, Portuguese, ASL, Cantonese, Japanese, Korean, Vietnamese, Arabic, Dutch, more... (if some need to be cut our because of overcrowding let me know OR we can make some big and others small)
- Below this it should have GROUP & PRIVATE LESSONS
- It should be colorful and make people think of things international - perhaps national flags in background? Or images of world famous monuments? Could be image of adutls in a classroom. Sth that gets people excited about travel and language learning
- It should have our contact info VERY large at bottom:
Zephyr Languages -
San Francisco, Silicon Valley & New York City
www.zephyrlanguagesf.com
415-926-1548
info@zephyrlanguagesf.com
(this can be smaller)
Two Halvorsen Plaza
Lobby 4
San Francisco, CA 94108

Hey Designers, please feel free to do a rough take on it. I don't need you to spend too much time, just give me a general idea of how you would make it look, then i know we can go from there later and refine it. Feel free to make it more of a quick sketch to show how you would do it.

Target Market(s)

adults from about 25-55 years old, educated, employed and typically world travellers

Industry/Entity Type

School

Colors
86cfc6
00a990
cadf82
acd036
9bcb3c
fbed22
f78f20
ffc214
f37122

Requirements
Must have
• Must be simple! Too many banners put way too much information and pictures. I want someone to walk by and immediately know we teach foreign languages. Must have bright colors and large font for languages offered
Should not have
• Should not be too full of images and design that distract the viewer from seeing the main thing I want them to see: that we teacher languages

```html
<!DOCTYPE html>
<html lang="en">
<head>
<meta charset="utf-8">
<title>Zephyr Languages – Rollup Banner</title>
<link rel="stylesheet" href="https://fonts.googleapis.com/css2?family=Baloo+2:wght@800&family=Mulish:wght@300;400;800&display=swap">
<style>
  :root {
    --teal: #00a990;
    --title-yellow: #fbed22;
    --band-yellow: #e2e04f;
    --frame-yellow: #fbed44;
    --logo-green: #1f9a3c;
    --orange: #f37122;
    --ink: #111111;
    --sky-top: #c9d4e0;
    --sky-bottom: #e4e8ec;
    --white: #ffffff;
  }
  * { margin: 0; padding: 0; box-sizing: border-box; }
  html, body { width: 1200px; height: 1200px; overflow: hidden; background: var(--white); }
  body { position: relative; font-family: "Mulish", sans-serif; }

  .banner {
    position: absolute; left: 379px; top: 29px;
    width: 442px; height: 1159px;
    background: var(--white);
    border: 1px solid var(--teal);
    overflow: hidden;
  }
  .banner > * { position: absolute; }

  .header-band {
    left: 0; top: 0; width: 100%; height: 76px;
    background: var(--teal);
    display: flex; align-items: center; justify-content: center;
  }
  .headline {
    font-family: "Baloo 2", "Arial Rounded MT Bold", sans-serif;
    font-weight: 800; font-size: 37px; line-height: 1;
    color: var(--title-yellow);
    letter-spacing: 0;
    white-space: nowrap;
    padding-top: 6px;
  }

  .flags-backdrop {
    left: 0; top: 76px; width: 100%; height: 334px;
    background: linear-gradient(180deg, var(--sky-top), var(--sky-bottom));
  }

  .brand-name {
    left: 0; top: 98px; width: 100%;
    text-align: center;
    font-family: "Mulish", sans-serif; font-weight: 800;
    font-size: 44px; line-height: 48px;
    color: var(--logo-green);
  }

  .language-list {
    left: 0; top: 228px; width: 100%;
    text-align: center;
    font-weight: 800; font-size: 22.5px; line-height: 29px;
    color: var(--ink);
  }

  .lessons-band {
    left: 0; top: 410px; width: 100%; height: 41px;
    background: var(--band-yellow);
    display: flex; align-items: center; justify-content: center;
    font-weight: 800; font-size: 27px; color: var(--ink);
    letter-spacing: 0.3px;
  }

  .classroom-photo {
    left: 0; top: 451px; width: 100%; height: 300px;
    background: linear-gradient(180deg, #e9eaea 0%, #c9c3bd 55%, #6f7568 100%);
  }
  .accent-strip {
    left: 0; top: 751px; width: 127px; height: 30px;
    background: var(--band-yellow);
  }
  .study-frame {
    left: 127px; top: 641px; width: 315px; height: 246px;
    background: var(--frame-yellow);
    opacity: 0.92;
  }
  .study-photo {
    left: 149px; top: 665px; width: 293px; height: 195px;
    background: linear-gradient(160deg, #cfd3cf 0%, #9a8e7e 50%, #4f3c2e 100%);
  }

  .contact {
    left: 0; top: 898px; width: 100%;
    text-align: center; color: var(--orange);
  }
  .contact-name {
    font-family: "Mulish", sans-serif; font-weight: 400;
    font-size: 40px; line-height: 50px;
  }
  .contact-lines {
    margin-top: 8px;
    font-weight: 800; font-size: 16.5px; line-height: 21.5px;
  }

  .address-band {
    left: 0; top: 1067px; width: 100%; height: 79px;
    background: var(--teal);
    color: var(--white);
    display: flex; flex-direction: column; align-items: center; justify-content: center;
    font-weight: 300; font-size: 16.5px; line-height: 20px;
  }
</style>
</head>
<body>
  <div class="banner">
    <header class="header-band">
      <h1 class="headline">Come Learn a Language!</h1>
    </header>

    <div class="flags-backdrop" role="img" aria-label="National flags waving on tall poles against a pale sky"></div>

    <div class="brand-name">Zephyr<br>Languages</div>

    <p class="language-list">
      Spanish, Chinese, French, Russian,<br>
      German, Italian, Farsi, Turkish,<br>
      Portuguese, ASL, Cantonese,<br>
      Japanese, Korean, Vietnamese,<br>
      Arabic, Dutch and more
    </p>

    <div class="lessons-band">GROUP &amp; PRIVATE LESSONS</div>

    <div class="classroom-photo" role="img" aria-label="Adult students seated at desks listening to a teacher in a classroom"></div>
    <div class="accent-strip"></div>
    <div class="study-frame"></div>
    <div class="study-photo" role="img" aria-label="Small group of adults studying together with books at a library table"></div>

    <section class="contact">
      <div class="contact-name">Zephyr Languages</div>
      <div class="contact-lines">
        San Francisco, Silicon Valley &amp; New York City<br>
        www.zephyrlanguagesf.com<br>
        415-926-1548<br>
        info@zephyrlanguagesf.com
      </div>
    </section>

    <footer class="address-band">
      <span>Two Halvorsen Plaza</span>
      <span>Lobby 4</span>
      <span>San Francisco, CA 94108</span>
    </footer>
  </div>
</body>
</html>
```